Website with a rustic Patriotic Feel

I am looking to design the
Home page I have a mock-up that has the essentials on it like our video, a small slideshow, our plans, and a coverage map, and a small sign up box to be sent a free SIM card.

Eligibility Page: Cool Background with a fill in box that lets the user know if their number is GSM or unlocked.

View Plans page: will have our plans hopefully in their colors with a cool background a walkthrough on Activation.

Activation: If you order your plan first then we send the SIM Card Basically another fill out sheet first name last name ICCID IMEI phone number email

, Contact Us: This is our Customer support page.

Swift Harbor ( this will be our About us page and will have a calendar of Community Volunteer Opportunities.. Right now I have a hodgepodge of different themes that I am going with for the web design. I would like it cohesive with the theme so all of it can fit together nicely.

At the Site map at the bottom we are looking for the basic Menu redirects. quick links to our T&Cs Customer Support and Follow US Buttons as well as a sign up for our Newsletter fill in.

Feel free to redo any of the ads. We are an MVNO like (Norvale Wireless) we provide network Voice and Data Plans our target audience is first Responders and Military. If you are wondering what that green map is its a coverage map to see where to best have coverage. Right now I have a website that uses CMS and HTML. If you are interested in doing a full redesign of our website we would love it.

Right now our website is www.kestrel-linknet.example if you need any additional information.

Target Market(s)

First Responders and Military

Coding

Coded - Design and coding required

Number of Pages Required

5+ page

Font styles to use
Sans Serif

Colors
0455a3
0493ce
f0474d
ffffff

Requirements
Must have
• Cohesive and have a powerpoint and coverage map
Should not have
• Anything flowery or kiddish

```html
<!DOCTYPE html>
<html lang="en">
<head>
<meta charset="utf-8">
<title>Kestrel Linknet – Eligibility</title>
<link href="https://fonts.googleapis.com/css2?family=Barlow:wght@400;500;600;700&display=swap" rel="stylesheet">
<style>
:root{
  --navy:#1b2556;
  --navy-text:#22307a;
  --red:#f52f2f;
  --blue:#3c98e0;
  --brand-blue:#4aa3f0;
  --sky:#b3e0fb;
  --paper:#ececec;
  --footer:#9b9b9b;
  --green:#2fa52f;
  --green-dark:#1f8a2a;
  --green-tint:#ebfde8;
  --text:#333;
  --white:#fff;
}
*{box-sizing:border-box;margin:0;padding:0}
html,body{width:1025px;height:1200px;overflow:hidden}
body{font-family:'Barlow',sans-serif;color:var(--text);position:relative;background:var(--paper)}
.abs{position:absolute}

/* header */
.site-header{left:0;top:0;width:1025px;height:64px;background:var(--navy)}
.brand{left:191px;top:23px;color:var(--brand-blue);font-weight:700;font-size:16px;line-height:18px;letter-spacing:.5px;white-space:nowrap}
.nav a{position:absolute;top:26px;color:var(--white);font-weight:600;font-size:9px;letter-spacing:.3px;text-decoration:none}
.btn-account{left:769px;top:22px;width:69px;height:22px;background:var(--red);color:#fff;font-weight:700;font-size:8.5px;display:flex;align-items:center;justify-content:center}

/* page title */
.page-title{left:0;top:64px;width:1025px;height:81px;background:var(--sky);text-align:center}
.page-title h1{margin-top:26px;font-size:22px;font-weight:700;color:var(--navy)}
.crumb{font-size:6px;color:var(--navy);margin-top:3px}
.crumb u{text-decoration:underline}

/* intro */
.intro-visual{left:185px;top:161px;width:217px;height:147px;background:linear-gradient(135deg,#d8d8d8,#8a8a8a 60%,#e7c9b2);border-radius:4px}
.intro-head{left:405px;top:196px;width:240px;font-size:14px;line-height:16px;color:#222;font-weight:400}
.intro-text{left:406px;top:239px;width:230px;font-size:7.8px;line-height:11.8px;color:#444;letter-spacing:-.1px}

/* checker */
.check-band{left:193px;top:308px;width:458px;height:47px;background:var(--blue);color:#fff;font-weight:700;font-size:15.5px;display:flex;align-items:center;justify-content:center}
.check-card{left:193px;top:355px;width:458px;height:200px;background:var(--white)}
.field{position:absolute;background:#fff;border:1px solid #d8d8d8;font-size:6.8px;color:#777;display:flex;align-items:center;padding-left:11px}
.btn-red{position:absolute;background:var(--red);color:#fff;font-weight:600;display:flex;align-items:center;justify-content:center}
.result{left:239px;top:428px;width:366px;height:83px;background:var(--green-tint);border:1.5px solid #a9e3a0;text-align:center}
.result small{display:block;margin-top:16px;font-size:7.5px;font-weight:600;color:#888}
.result strong{display:block;color:var(--green-dark);font-size:19px;line-height:18px;font-weight:700;margin-top:3px}
.result svg{position:absolute;left:26px;top:27px}

/* faq */
.faq-title{left:191px;top:590px;font-size:16px;font-weight:700;color:var(--navy-text)}
.faq-open{left:192px;top:626px;width:459px;height:27px;background:#b1b1b1;color:#fff;font-size:9px;font-weight:600;padding-left:13px;display:flex;align-items:center}
.faq-open span,.faq-item span{position:absolute;right:20px}
.faq-body{left:192px;top:653px;width:459px;height:73px;background:#fff;padding:15px 19px;font-size:7px;line-height:11.7px;color:#555}
.faq-item{position:absolute;left:192px;width:459px;height:27px;border-bottom:1px solid #c9cbe0;font-size:9.2px;font-weight:600;color:#333;padding-left:13px;display:flex;align-items:center}

/* sidebar */
.sim-card{left:697px;top:174px;width:170px;height:164px;background:#fff;text-align:center}
.sim-card p{margin-top:23px;font-size:8.5px;color:#333}
.sim-card h3{color:var(--red);font-size:13px;line-height:13.5px;font-weight:600;margin-top:2px}
.promo{position:absolute;left:697px;width:170px;background:var(--navy);text-align:center;color:#fff}
.promo-visual{width:170px;background:linear-gradient(180deg,#f2f2f2,#9aa0aa)}
.promo h4{font-weight:700;line-height:14px}
.btn-green{display:block;margin:0 auto;width:146px;height:25px;background:var(--green);color:#fff;font-size:7.8px;font-weight:700;line-height:25px}

/* location */
.footer-bg{left:0;top:966px;width:1025px;height:234px;background:var(--footer)}
.locator{left:193px;top:918px;width:637px;height:77px;background:#fff;box-shadow:0 0 6px rgba(0,0,0,.08)}
.locator h2{position:absolute;left:45px;top:26px;font-size:21px;font-weight:500;color:var(--navy-text)}

/* footer */
.foot-col{position:absolute;top:1026px}
.foot-col h5{color:#fff;font-size:9px;font-weight:600;margin-bottom:5px}
.foot-col a{display:block;color:#fff;font-size:7px;text-decoration:none;line-height:17px}
.social{display:flex;gap:11px;margin-top:4px}
.social span{width:12px;height:12px;border:1.5px solid #fff;border-radius:3px;display:block}
.social span.round{border-radius:50%}
.copyright{left:0;top:1178px;width:1025px;text-align:center;color:#fff;font-size:5.8px}
</style>
</head>
<body>

<header class="site-header abs">
  <div class="brand abs">KESTREL LINKNET</div>
  <nav class="nav">
    <a style="left:361px">HOME</a>
    <a style="left:419px">VIEW PLANS</a>
    <a style="left:496px">ACTIVATE TODAY</a>
    <a style="left:592px">CONTACT US</a>
    <a style="left:669px">SWIFT HARBOR</a>
  </nav>
  <div class="btn-account abs">MY ACCOUNT</div>
</header>

<section class="page-title abs">
  <h1>ELIGIBILITY</h1>
  <div class="crumb"><u>HOME</u> / ELIGIBILITY</div>
</section>

<div class="intro-visual abs" role="img" aria-label="Hands holding a smartphone over a laptop keyboard with a small potted plant"></div>
<h2 class="intro-head abs">Lorem ipsum dolor sit amet, consectetur adipiscing elit.</h2>
<p class="intro-text abs">Lorem ipsum dolor sit amet, consectetur adipiscing elit. Donec sit amet metus efficitur, mattis eros non, ultrices libero. Fusce congue, eros ut gravida posuere, nulla mi pulvinar nibh, et pellentesque libero erat ut lacus.</p>

<div class="check-band abs">CHECK YOUR MOBILE NO IS GSM OR UNLOCKED</div>
<div class="check-card abs"></div>
<div class="field" style="left:240px;top:380px;width:242px;height:33px">Mobile no : &nbsp;+91 9800012345</div>
<div class="btn-red" style="left:482px;top:380px;width:123px;height:33px;font-size:11.5px">SUBMIT</div>

<div class="result abs">
  <svg width="28" height="28" viewBox="0 0 28 28"><circle cx="14" cy="14" r="12" fill="none" stroke="#1f8a2a" stroke-width="2.2"/><path d="M8 14.5l4 4 8-8" fill="none" stroke="#1f8a2a" stroke-width="2.4" stroke-linecap="round" stroke-linejoin="round"/></svg>
  <small>Your Mobile no :</small>
  <strong>+91 9800012345<br>is unclocked</strong>
</div>

<h2 class="faq-title abs">FREQUENTLY ASKED QUESTIONS</h2>
<div class="faq-open abs">Lorem ipsum dolor sit amet, consectetur adipiscing elit.<span>-</span></div>
<p class="faq-body abs">Lorem ipsum dolor sit amet, consectetur adipiscing elit. Sed nec vehicula urna. Proin pulvinar laoreet tellus sed viverra. Morbi non tempor nulla, id varius lorem. Donec a diam tristique turpis sagittis vulputate sed molestie ante. Vivamus porttitor ornare erat, eget finibus dolor feugiat id. Pellentesque elementum urna ac magna venenatis, vel cursus ligula dignissim.</p>
<div class="faq-item" style="top:726px">In tincidunt erat quis aliquet rutrum.<span>+</span></div>
<div class="faq-item" style="top:754px">Maecenas ultricies turpis quis lorem fringilla imperdiet.<span>+</span></div>
<div class="faq-item" style="top:782px">Nullam at lorem et risus sodales ullamcorper.<span>+</span></div>
<div class="faq-item" style="top:810px;border-bottom:none">Mauris et diam nec est luctus aliquam suscipit et mi.<span>+</span></div>

<aside>
  <div class="sim-card abs">
    <p>Is your smartphone ready for</p>
    <h3>KESTREL LINKNET<br>connection?</h3>
  </div>
  <div class="field" style="left:715px;top:253px;width:141px;height:32px">Enter your email</div>
  <div class="btn-red" style="left:715px;top:292px;width:140px;height:33px;font-size:11px">GET SIM CARD NOW</div>

  <div class="promo" style="top:355px;height:179px">
    <div class="promo-visual" style="height:107px" role="img" aria-label="Police officer, paramedic and firefighter standing together"></div>
    <h4 style="font-size:13px;margin-top:6px">FIRST RESPONDER<br>DISCOUNT</h4>
    <span class="btn-green" style="margin-top:3px">CLICK HERE FOR DISCOUNT CODE</span>
  </div>
  <div class="promo" style="top:551px;height:179px">
    <div class="promo-visual" style="height:113px;background:linear-gradient(180deg,#3a3a36,#6b6b58)" role="img" aria-label="Soldier in camouflage uniform taking a video call on a phone"></div>
    <h4 style="font-size:16px;margin-top:10px">MILITARY DISCOUNT</h4>
    <span class="btn-green" style="margin-top:5px">CLICK HERE FOR DISCOUNT CODE</span>
  </div>
</aside>

<div class="footer-bg abs"></div>
<section class="locator abs">
  <h2>SEARCH FOR A LOCATION</h2>
</section>
<div class="field" style="left:507px;top:941px;width:178px;height:33px">Enter your mobile no</div>
<div class="btn-red" style="left:685px;top:941px;width:90px;height:33px;font-size:11.5px">SEARCH NOW</div>

<footer>
  <div class="foot-col" style="left:195px"><h5>QUICK LINKS</h5><a>Home</a><a>Catalog</a><a>View Plans</a><a>Activate Today</a><a>Contact Us</a><a>Swift Harbor</a></div>
  <div class="foot-col" style="left:373px"><h5>DISCLAIMERS</h5><a>Terms &amp; Conditions</a><a>Activating Your Service</a><a>Acceptable Use Policy</a><a>Wireless Privacy Policy</a><a>Coverage Map</a></div>
  <div class="foot-col" style="left:549px"><h5>CUSTOMER SUPPORT</h5><a>View Plans</a><a>Contact Us</a><a>Phone: +1(833)555-0142</a></div>
  <div class="foot-col" style="left:721px"><h5>FOLLOW US</h5><div class="social"><span></span><span class="round"></span><span></span></div></div>
  <div class="copyright abs">COPYRIGHT © 2020 KESTREL LINKNET ALL RIGHTS RESERVED</div>
</footer>

</body>
</html>
```